Condom Poster Project

we are in need a design for a poster 12"x15" for our long love condoms brand TWO TIDES,the USP=Unique selling proposition is the condom extends the time of making love by the benzocaine inside it.

The following points should be in the design:
1)our phone number(5184-6027),use the phone logo face to the phone number.
2)our email address(solvendrapharm@quillmail.fr ),use the email logo face to the email address.
3)the packagings are in the attached file.
4)our slogan(LOVE HER LONGER) (PLAISIR + ENDURANCE + SECURITE)
5)You can copy the appropriated pictures from pixorvane and if you win we will buy it as we have an account with this company,so be creative.
6)the phone number and email should be located at the bottom in one line very small as they are not an important factors.Please make them smaller.
Updates

new packagings have been loaded and modification has been made on the slogan.

new packaging pictures have been uploaded

we just uploaded new packaging pictures.

Project Deadline Extended
Reason: we need more creativity.

Target Market(s)

15 to 30 years old men

Industry/Entity Type

It Company

Requirements
Must have
• must have the packaging You can copy the appropriated pictures from pixorvane and if you win we will buy it as we have an account with this company,so be creative.
Nice to have
• You can copy the appropriated pictures from pixorvane and if you win we will buy it as we have an account with this company,so be creative.
Should not have
• should not have any other language than french as it is speaking language in our country.

```html
<!DOCTYPE html>
<html lang="fr">
<head>
<meta charset="utf-8">
<title>TWO TIDES – Love Her Longer</title>
<link rel="stylesheet" href="https://fonts.googleapis.com/css2?family=Oswald:wght@700&family=Open+Sans:wght@700;800&family=Parisienne&display=swap">
<style>
  :root {
    --stage: #3a3a3a;
    --paper-light: #ffffff;
    --paper-shade: #e4e4e4;
    --love-red: #e3262b;
    --script-grey: #5a5a5a;
    --ink: #3c3c3c;
    --heart-red: #d81f26;
    --heart-deep: #a30f16;
    --pack-light: #eeeeee;
    --pack-shade: #c9c9cc;
  }
  * { margin: 0; padding: 0; box-sizing: border-box; }
  html, body { width: 1200px; height: 1000px; overflow: hidden; }
  body {
    background: var(--stage);
    display: flex;
    align-items: center;
    justify-content: center;
  }
  .poster {
    position: relative;
    width: 760px;
    height: 950px;
    background: radial-gradient(ellipse at 50% 45%, var(--paper-light) 40%, var(--paper-shade) 100%);
    overflow: hidden;
  }
  .headline-love {
    position: absolute;
    left: 40px;
    top: 14px;
    font-family: "Oswald", "Arial Narrow", sans-serif;
    font-weight: 700;
    font-size: 150px;
    line-height: 1;
    color: var(--love-red);
    transform: skewX(-8deg);
    letter-spacing: -2px;
  }
  .headline-her {
    position: absolute;
    left: 240px;
    top: 150px;
    font-family: "Parisienne", cursive;
    font-size: 110px;
    line-height: 1;
    color: var(--script-grey);
  }
  .headline-longer {
    position: absolute;
    left: 405px;
    top: 192px;
    font-family: "Oswald", "Arial Narrow", sans-serif;
    font-weight: 700;
    font-size: 82px;
    line-height: 1;
    color: var(--love-red);
    transform: skewX(-6deg);
  }
  .hearts-art {
    position: absolute;
    left: 120px;
    top: 320px;
    width: 540px;
    height: 400px;
    background: radial-gradient(ellipse at 50% 48%, var(--heart-red) 0%, var(--heart-deep) 55%, rgba(163,15,22,0) 72%);
  }
  .pack-shot {
    position: absolute;
    left: 190px;
    top: 760px;
    width: 110px;
    height: 130px;
    border-radius: 6px;
    background: linear-gradient(135deg, var(--pack-light), var(--pack-shade));
  }
  .benefits {
    position: absolute;
    left: 325px;
    top: 765px;
    list-style: none;
    font-family: "Open Sans", Arial, sans-serif;
    font-weight: 800;
    font-size: 32px;
    line-height: 40px;
    letter-spacing: 2px;
    color: var(--ink);
  }
  .contact-line {
    position: absolute;
    left: 190px;
    bottom: 22px;
    display: flex;
    gap: 40px;
    font-family: "Open Sans", Arial, sans-serif;
    font-weight: 700;
    font-size: 11px;
    color: var(--ink);
  }
</style>
</head>
<body>
  <main class="poster">
    <h1 class="headline">
      <span class="headline-love">LOVE</span>
      <span class="headline-her">her</span>
      <span class="headline-longer">LONGER</span>
    </h1>
    <div class="hearts-art" role="img" aria-label="Deux grands cœurs rouges brillants entourés de petits cœurs"></div>
    <div class="pack-shot" role="img" aria-label="Emballage de préservatifs TWO TIDES"></div>
    <ul class="benefits">
      <li>PLAISIR</li>
      <li>ENDURANCE</li>
      <li>SECURITE</li>
    </ul>
    <footer class="contact-line">
      <span class="contact-phone">phone : 5184-6027</span>
      <span class="contact-email">solvendrapharm@quillmail.fr</span>
    </footer>
  </main>
</body>
</html>
```